Veltrix Global Policy Document/Report Template for consistent document outputs

We need a policy document/report template that we can disseminate to staff so all produced documents look the same, and less formatting has to be done each time a policy or report is started.
VGL applies the power of biological science, physical science, and IT to solve the most challenging mission problems encompassing Forensics, Biometrics, Weapons Technical and Identity Intelligence, CBRNE, CWMD, and Public Health initiatives. Here is a list of requirements for the document:
• Cover page
o Include full logo
o Title
o Possibly a subtitle
o Version #
o Date
o We want a common look that all policy documents will follow, and it is easy to recognize
o Some color and a unique look and feel
• Header and Footer (2nd page on)
o Both header and footer must include this language: “Confidential and Proprietary - For Veltrix Global Internal Use Only,” so it appears at the top and bottom of the page
o The document title must be in either the header or footer
• Header (after first page)
o Include logo
• Footer (not counting title page)
o Must include date, and page X of Y
• 4 levels of headings, numbered 1, 1.1, 1.1.1, 1.1.1.1
• 4 levels of bullets with color/style
• Design for a callout box
• Design or a box containing a quote
• Two table designs
• Pages (other than the title page)
o Pages are primarily white
o Colors for accent and visual interest

Finally, our corporate font is Source Sans Pro.
The swirl pattern on our logo has no special meaning (but feel free to use it as a design element).

Font styles to use
Other font styles liked:
• Source Sans Pro

Requirements
Must have
• See description for more information: Cover page, header and footer, multiple heading levels, callout box, tables

```html
<!DOCTYPE html>
<html lang="en">
<head>
<meta charset="utf-8">
<title>Veltrix Global Document Template</title>
<link href="https://fonts.googleapis.com/css2?family=Poppins:wght@400;500;600;700&display=swap" rel="stylesheet">
<style>
  :root {
    --stage: #0e0e0e;
    --indigo: #231a6e;
    --indigo-deep: #1d1460;
    --crimson: #a3063f;
    --plum: #6e1a6a;
    --violet: #4b1fa0;
    --row-pink: #e7d6e4;
    --row-lilac: #d5cef0;
    --callout-bg: #f3eefb;
    --text: #2c2c2c;
    --muted: #444;
    --white: #ffffff;
  }
  * { box-sizing: border-box; margin: 0; padding: 0; }
  html, body { width: 948px; height: 1200px; overflow: hidden; background: var(--stage); }
  body { font-family: "Poppins", sans-serif; color: var(--text); position: relative; }

  .page { position: absolute; width: 434px; height: 563px; background: var(--white); overflow: hidden; }
  .page--cover { left: 26px; top: 22px; }
  .page--text { left: 484px; top: 22px; }
  .page--tables { left: 24px; top: 616px; width: 435px; }
  .page--headings { left: 484px; top: 616px; }

  .abs { position: absolute; }

  /* cover */
  .cover-art { position: absolute; left: 0; top: 0; width: 434px; height: 390px; }
  .cover-title { position: absolute; left: 0; top: 0; width: 100%; text-align: center; color: var(--white); }
  .cover-title h1 { font-weight: 400; font-size: 25px; position: absolute; top: 139px; width: 100%; }
  .cover-title p { font-size: 16.5px; position: absolute; top: 180px; width: 100%; }
  .presenter { left: 27px; top: 436px; }
  .presenter-name { font-size: 13.5px; color: var(--indigo); }
  .presenter-role { font-size: 11px; color: var(--muted); margin-top: 1px; }
  .doc-meta { font-size: 8.4px; color: var(--crimson); font-weight: 500; margin-top: 8px; line-height: 13px; }
  .brand { display: flex; align-items: center; gap: 8px; }
  .brand-dot { border-radius: 50%; flex: none; }
  .brand-name { font-weight: 700; line-height: 1; letter-spacing: -0.5px; }
  .brand--cover { left: 264px; top: 418px; }
  .brand--cover .brand-dot { width: 24px; height: 24px; background: var(--crimson); }
  .brand--cover .brand-name { font-size: 46px; color: var(--indigo); }
  .band { position: absolute; left: 0; bottom: 0; width: 100%; height: 18px;
    background: linear-gradient(90deg, #2a1a86 0%, #6b2bd8 25%, #b13fe0 40%, #5a1b8c 60%, #8d0d4a 85%, #b0063d 100%); }

  /* inner header */
  .header { position: absolute; left: 0; top: 0; width: 100%; height: 100px; }
  .header-title { position: absolute; left: 14px; top: 11px; font-size: 16.5px; font-weight: 600; color: var(--white); }
  .header-note { position: absolute; left: 14px; top: 36px; font-size: 6.2px; color: var(--white); opacity: 0.9; }
  .brand--header { right: 20px; top: 24px; gap: 5px; }
  .brand--header .brand-dot { width: 12px; height: 12px; background: var(--white); }
  .brand--header .brand-name { font-size: 24px; color: var(--white); }

  /* footer */
  .footer { position: absolute; left: 0; bottom: 0; width: 100%; height: 19px;
    background: linear-gradient(90deg, #2b1874 0%, #3b1c8a 40%, #4a1a86 70%, #5a1680 100%);
    border-top: 1px solid #7d6ad0;
    color: var(--white); font-size: 6.3px; display: flex; align-items: center; justify-content: space-between; padding: 0 9px; white-space: nowrap; }
  .footer strong { font-weight: 600; }

  /* headings & text */
  .para-heading { position: absolute; left: 18px; top: 89px; font-size: 16.5px; font-weight: 700; color: var(--indigo); }
  .body-copy { position: absolute; left: 19px; width: 404px; font-size: 10.3px; line-height: 15.6px; color: var(--text); }
  .subtext { position: absolute; left: 19px; top: 250px; font-size: 11px; font-weight: 700; color: var(--crimson); }

  /* tables */
  .table-title { position: absolute; left: 18px; font-size: 16px; font-weight: 700; color: var(--indigo); }
  .codes { position: absolute; left: 19px; top: 118px; width: 394px; font-size: 9px; }
  .codes-row { position: relative; height: 26px; margin-bottom: 2.8px; display: flex; align-items: center; color: var(--text); letter-spacing: 0.2px; }
  .codes-row span { position: absolute; }
  .codes-row .sr { left: 11px; }
  .codes-row .desc { left: 48px; }
  .codes-row .code { left: 339px; }
  .codes-head { background: var(--indigo); color: var(--white); font-weight: 600; font-size: 9.6px; height: 27px; margin-bottom: 2.5px; }
  .codes-head .code { left: 311px; }
  .codes-row--pink { background: var(--row-pink); }
  .codes-row--lilac { background: var(--row-lilac); }
  .codes-row--active { color: #4a3aa8; }

  .pricing { position: absolute; top: 330px; width: 93px; text-align: center; }
  .pricing-head { height: 27px; background: var(--indigo); color: var(--white); font-size: 9.8px; font-weight: 600; display: flex; align-items: center; justify-content: center; }
  .pricing-price { height: 29px; font-size: 11.5px; font-weight: 700; color: #111; display: flex; align-items: center; justify-content: center; }
  .pricing-cell { height: 26.5px; margin-bottom: 2.5px; font-size: 9px; color: var(--muted); display: flex; align-items: center; justify-content: center; }
  .pricing-cell:nth-child(odd) { background: var(--row-lilac); }
  .pricing-cell:nth-child(even) { background: var(--row-pink); }
  .pricing-foot { height: 6px; background: var(--plum); margin-top: 1.5px; }

  /* heading levels */
  .h1 { position: absolute; left: 19px; top: 120px; font-size: 14.5px; font-weight: 500; color: var(--crimson); }
  .h1-copy { position: absolute; left: 19px; top: 137px; width: 412px; font-size: 8.8px; line-height: 13px; color: var(--text); }
  .h2 { position: absolute; left: 31px; top: 173px; font-size: 12px; font-weight: 500; color: var(--indigo); }
  .h3 { position: absolute; left: 44px; top: 276px; font-size: 10.4px; font-weight: 600; color: var(--indigo); }
  .h4 { position: absolute; left: 56px; top: 377px; font-size: 8.8px; font-weight: 600; color: var(--indigo); }
  .list { position: absolute; list-style: none; }
  .list li { display: flex; align-items: center; }
  .list--l1 { left: 31px; top: 194px; font-size: 10px; }
  .list--l1 li { height: 18.5px; gap: 5px; }
  .list--l1 svg { width: 9px; height: 9px; }
  .list--l2 { left: 46px; top: 294px; font-size: 9.6px; }
  .list--l2 li { height: 18.5px; gap: 6px; }
  .ring { width: 5.5px; height: 5.5px; border: 1.4px solid var(--indigo); border-radius: 50%; }
  .list--l3 { left: 59px; top: 395px; font-size: 7.7px; }
  .list--l3 li { height: 18.6px; gap: 5px; }
  .dot { width: 5.5px; height: 5.5px; background: var(--crimson); border-radius: 50%; }

  /* callout & quote */
  .callout { position: absolute; left: 236px; top: 180px; width: 180px; padding: 10px 12px;
    background: var(--callout-bg); border-left: 4px solid var(--crimson); }
  .callout-title { font-size: 9.5px; font-weight: 600; color: var(--crimson); margin-bottom: 4px; }
  .callout-text { font-size: 7.8px; line-height: 12px; color: var(--text); }
  .quote { position: absolute; left: 236px; top: 300px; width: 180px; padding: 12px 12px 10px 12px;
    background: var(--indigo); color: var(--white); border-radius: 0 14px 0 14px; }
  .quote-mark { font-size: 26px; line-height: 18px; font-weight: 700; color: #d07ab8; }
  .quote-text { font-size: 8.4px; line-height: 13px; font-style: italic; margin-top: 2px; }
  .quote-by { font-size: 7.4px; font-weight: 600; margin-top: 6px; color: #e4c6ea; }
</style>
</head>
<body>

<!-- Cover -->
<section class="page page--cover">
  <svg class="cover-art" viewBox="0 0 434 390" role="img" aria-label="Laboratory science photograph with molecular structure overlay in crimson, magenta and indigo tones">
    <defs>
      <linearGradient id="coverFill" x1="1" y1="0" x2="0" y2="1">
        <stop offset="0" stop-color="#a5093e"/>
        <stop offset="0.35" stop-color="#b5307f"/>
        <stop offset="0.65" stop-color="#7a2a9c"/>
        <stop offset="1" stop-color="#2c1f8e"/>
      </linearGradient>
      <linearGradient id="coverLine" x1="0" y1="0" x2="1" y2="0">
        <stop offset="0" stop-color="#251770"/>
        <stop offset="0.6" stop-color="#4a1a72"/>
        <stop offset="1" stop-color="#a3063f"/>
      </linearGradient>
    </defs>
    <path d="M0 0H434V343C410 335 360 326 300 332C230 340 180 372 110 377C70 380 30 370 0 341Z" fill="url(#coverFill)"/>
    <path d="M2 344C32 372 72 382 110 379C180 374 230 342 300 334C360 328 410 337 434 345" fill="none" stroke="url(#coverLine)" stroke-width="4"/>
  </svg>
  <div class="cover-title">
    <h1>Project Title here</h1>
    <p>Subtext here</p>
  </div>
  <div class="abs presenter">
    <p class="presenter-name">Persentator Name Here</p>
    <p class="presenter-role">Designation here</p>
    <p class="doc-meta">Version 1.0<br>Date: 01 January 2025</p>
  </div>
  <div class="abs brand brand--cover">
    <span class="brand-dot"></span>
    <span class="brand-name">VGL</span>
  </div>
  <div class="band"></div>
</section>

<!-- Inner page: paragraphs -->
<section class="page page--text">
  <svg class="header" viewBox="0 0 434 100" role="img" aria-label="Purple and magenta laboratory photograph header band">
    <defs>
      <linearGradient id="headFillA" x1="0" y1="0" x2="1" y2="0">
        <stop offset="0" stop-color="#3b1a8c"/>
        <stop offset="0.5" stop-color="#8a2a98"/>
        <stop offset="1" stop-color="#b0206e"/>
      </linearGradient>
    </defs>
    <path d="M0 0H434V62C410 80 385 88 348 86C260 80 120 56 0 60Z" fill="url(#headFillA)"/>
    <path d="M0 60C120 56 260 80 348 86C385 88 410 80 434 62" fill="none" stroke="#1d1460" stroke-width="3"/>
  </svg>
  <h2 class="header-title">Inner Page Title here</h2>
  <p class="header-note">Confidential and Proprietary - For Veltrix Global Internal Use Only</p>
  <div class="abs brand brand--header"><span class="brand-dot"></span><span class="brand-name">VGL</span></div>

  <h3 class="para-heading">Pargraph Heading Here</h3>
  <p class="body-copy" style="top:129px">Lorem ipsum dolor sit amet, consectetur adipiscing elit, sed do eiusmod tempor incididunt ut labore et dolore magna aliqua. Quis ipsum suspendisse ultrices gravida. Risus commodo viverra maecenas accumsan lacus vel facilisis. Lorem ipsum dolor sit amet, consectetur adipiscing elit, sed do eiusmod tempor incididunt ut labore et dolore magna aliqua. Quis ipsum suspendisse ultrices gravida. Risus commodo viverra maecenas accumsan lacus vel facilisis.</p>
  <p class="subtext">Subtext here</p>
  <p class="body-copy" style="top:268px">Lorem ipsum dolor sit amet, consectetur adipiscing elit, sed do eiusmod tempor incididunt ut labore et dolore magna aliqua. Quis ipsum suspendisse ultrices gravida. Risus commodo viverra maecenas accumsan lacus vel facilisis. Lorem ipsum dolor sit amet, consectetur adipiscing elit, sed do eiusmod tempor incididunt ut labore et dolore magna aliqua. Quis ipsum suspendisse ultrices gravida. Risus commodo viverra maecenas accumsan lacus vel facilisis.</p>
  <p class="body-copy" style="top:393px">Lorem ipsum dolor sit amet, consectetur adipiscing elit, sed do eiusmod tempor incididunt ut labore et dolore magna aliqua. Quis ipsum suspendisse ultrices gravida. Risus commodo viverra maecenas accumsan lacus vel facilisis. Lorem ipsum dolor sit amet, consectetur adipiscing elit, sed do eiusmod tempor incididunt ut labore et dolore magna aliqua. Quis ipsum suspendisse ultrices gravida. Risus commodo viverra maecenas accumsan lacus vel facilisis.</p>

  <footer class="footer"><span>www.veltrixglobal.com</span><strong>Project Title here · 01 Jan 2025 · Page 1 of 3</strong></footer>
</section>

<!-- Inner page: tables -->
<section class="page page--tables">
  <svg class="header" viewBox="0 0 435 100" role="img" aria-label="Purple and magenta laboratory photograph header band">
    <defs>
      <linearGradient id="headFillB" x1="0" y1="0" x2="1" y2="0">
        <stop offset="0" stop-color="#3b1a8c"/>
        <stop offset="0.5" stop-color="#8a2a98"/>
        <stop offset="1" stop-color="#b0206e"/>
      </linearGradient>
    </defs>
    <path d="M0 0H435V62C411 80 386 88 349 86C261 80 120 56 0 60Z" fill="url(#headFillB)"/>
    <path d="M0 60C120 56 261 80 349 86C386 88 411 80 435 62" fill="none" stroke="#1d1460" stroke-width="3"/>
  </svg>
  <h2 class="header-title">Inner Page Title here</h2>
  <p class="header-note">Confidential and Proprietary - For Veltrix Global Internal Use Only</p>
  <div class="abs brand brand--header"><span class="brand-dot"></span><span class="brand-name">VGL</span></div>

  <h3 class="table-title" style="top:89px">Tabular Data design 1</h3>
  <div class="codes">
    <div class="codes-row codes-head"><span class="sr">Sr.</span><span class="desc">Description title here</span><span class="code">NAICS Codes</span></div>
    <div class="codes-row codes-row--pink"><span class="sr">01</span><span class="desc">Data Processing, Hosting, and Related Services</span><span class="code">518210</span></div>
    <div class="codes-row codes-row--lilac codes-row--active"><span class="sr">02</span><span class="desc">Data Processing, Hosting, and Related Services</span><span class="code">518210</span></div>
    <div class="codes-row codes-row--pink"><span class="sr">01</span><span class="desc">Data Processing, Hosting, and Related Services</span><span class="code">518210</span></div>
    <div class="codes-row codes-row--lilac"><span class="sr">02</span><span class="desc">Data Processing, Hosting, and Related Services</span><span class="code">518210</span></div>
    <div class="codes-row codes-row--pink"><span class="sr">01</span><span class="desc">Data Processing, Hosting, and Related Services</span><span class="code">518210</span></div>
  </div>

  <h3 class="table-title" style="top:299px">Tabular Data design 2</h3>
  <div class="pricing" style="left:19px">
    <div class="pricing-head">Table Title</div><div class="pricing-price">$100</div>
    <div><div class="pricing-cell">Featured One</div><div class="pricing-cell">Featured One</div><div class="pricing-cell">Featured One</div><div class="pricing-cell">Featured One</div></div>
    <div class="pricing-foot"></div>
  </div>
  <div class="pricing" style="left:120px; width:98px">
    <div class="pricing-head">Table Title</div><div class="pricing-price">$100</div>
    <div><div class="pricing-cell">Featured One</div><div class="pricing-cell">Featured One</div><div class="pricing-cell">Featured One</div><div class="pricing-cell">Featured One</div></div>
    <div class="pricing-foot"></div>
  </div>
  <div class="pricing" style="left:225px; width:92px">
    <div class="pricing-head">Table Title</div><div class="pricing-price">$100</div>
    <div><div class="pricing-cell">Featured One</div><div class="pricing-cell">Featured One</div><div class="pricing-cell">Featured One</div><div class="pricing-cell">Featured One</div></div>
    <div class="pricing-foot"></div>
  </div>
  <div class="pricing" style="left:325px; width:86px">
    <div class="pricing-head">Table Title</div><div class="pricing-price">$100</div>
    <div><div class="pricing-cell">Featured One</div><div class="pricing-cell">Featured One</div><div class="pricing-cell">Featured One</div><div class="pricing-cell">Featured One</div></div>
    <div class="pricing-foot"></div>
  </div>

  <footer class="footer"><span>Confidential and Proprietary - For Veltrix Global Internal Use Only,</span><strong>Project Title here · 01 Jan 2025 · Page 2 of 3</strong></footer>
</section>

<!-- Inner page: heading levels -->
<section class="page page--headings">
  <svg class="header" viewBox="0 0 434 100" role="img" aria-label="Purple and magenta laboratory photograph header band">
    <defs>
      <linearGradient id="headFillC" x1="0" y1="0" x2="1" y2="0">
        <stop offset="0" stop-color="#3b1a8c"/>
        <stop offset="0.5" stop-color="#8a2a98"/>
        <stop offset="1" stop-color="#b0206e"/>
      </linearGradient>
    </defs>
    <path d="M0 0H434V62C410 80 385 88 348 86C260 80 120 56 0 60Z" fill="url(#headFillC)"/>
    <path d="M0 60C120 56 260 80 348 86C385 88 410 80 434 62" fill="none" stroke="#1d1460" stroke-width="3"/>
  </svg>
  <h2 class="header-title">Inner Page Title here</h2>
  <p class="header-note">Confidential and Proprietary - For Veltrix Global Internal Use Only</p>
  <div class="abs brand brand--header"><span class="brand-dot"></span><span class="brand-name">VGL</span></div>

  <h3 class="para-heading">Pargraph Heading Here</h3>
  <h4 class="h1">1. Main Heading</h4>
  <p class="h1-copy">Lorem ipsum dolor sit amet, consectetur adipiscing elit, sed do eiusmod tempor incididunt ut labore et dolore magna aliqua. Quis ipsum suspendisse ultrices gravida.</p>

  <h5 class="h2">1.1 Sub Heading</h5>
  <ul class="list list--l1">
    <li><svg viewBox="0 0 10 10"><circle cx="5" cy="5" r="4" fill="none" stroke="#231a6e" stroke-width="1.2"/><path d="M3 5.2 4.6 6.7 8.6 2.4" fill="none" stroke="#231a6e" stroke-width="1.3"/></svg>Bullet points here</li>
    <li><svg viewBox="0 0 10 10"><circle cx="5" cy="5" r="4" fill="none" stroke="#231a6e" stroke-width="1.2"/><path d="M3 5.2 4.6 6.7 8.6 2.4" fill="none" stroke="#231a6e" stroke-width="1.3"/></svg>Bullet points here</li>
    <li><svg viewBox="0 0 10 10"><circle cx="5" cy="5" r="4" fill="none" stroke="#231a6e" stroke-width="1.2"/><path d="M3 5.2 4.6 6.7 8.6 2.4" fill="none" stroke="#231a6e" stroke-width="1.3"/></svg>Bullet points here</li>
    <li><svg viewBox="0 0 10 10"><circle cx="5" cy="5" r="4" fill="none" stroke="#231a6e" stroke-width="1.2"/><path d="M3 5.2 4.6 6.7 8.6 2.4" fill="none" stroke="#231a6e" stroke-width="1.3"/></svg>Bullet points here</li>
  </ul>

  <h6 class="h3">1.1.1 Sub Sub Heading</h6>
  <ul class="list list--l2">
    <li><span class="ring"></span>Bullet points here</li>
    <li><span class="ring"></span>Bullet points here</li>
    <li><span class="ring"></span>Bullet points here</li>
    <li><span class="ring"></span>Bullet points here</li>
  </ul>

  <p class="h4">1.1.1.1 Level 4 Heading</p>
  <ul class="list list--l3">
    <li><span class="dot"></span>Bullet points here</li>
    <li><span class="dot"></span>Bullet points here</li>
    <li><span class="dot"></span>Bullet points here</li>
    <li><span class="dot"></span>Bullet points here</li>
  </ul>

  <aside class="callout">
    <p class="callout-title">Callout Title Here</p>
    <p class="callout-text">Lorem ipsum dolor sit amet, consectetur adipiscing elit, sed do eiusmod tempor incididunt ut labore et dolore magna aliqua.</p>
  </aside>

  <blockquote class="quote">
    <p class="quote-mark">“</p>
    <p class="quote-text">Lorem ipsum dolor sit amet, consectetur adipiscing elit, sed do eiusmod tempor incididunt ut labore.</p>
    <p class="quote-by">— Quote Author Name</p>
  </blockquote>

  <footer class="footer"><span>Confidential and Proprietary - For Veltrix Global Internal Use Only,</span><strong>Project Title here · 01 Jan 2025 · Page 3 of 3</strong></footer>
</section>

</body>
</html>
```